Dallas Texas Special Event Center Flyer

Need a new brochure (small 8.5 x 11 tri-fold) for an event center in Dallas, Texas area. It is located on a golf course and is ideal for weddings, quinceaneras, retirement parties, etc. Is best known for weddings. There is no logo for the event center. I have attached the prior brochure, which is not professional. We do not have any site photos.

Target Market(s)

people seeking special event space in dallas, texas area. Brides, meeting planners, etc.

Industry/Entity Type

Golf Course

Font styles to use
Script
Other font styles liked:
• combine serif and some use of script ok

Requirements
Must have
• lots of photos - see attached

```html
<!DOCTYPE html>
<html lang="en">
<head>
<meta charset="utf-8">
<title>The Event Hall at Willowbrook – Tri-fold Brochure</title>
<link rel="stylesheet" href="https://fonts.googleapis.com/css2?family=Cinzel:wght@400;700&family=Raleway:wght@400;800&display=swap">
<style>
  :root {
    --stage: #808080;
    --paper: #ffffff;
    --ink: #6b5c59;
    --ink-soft: #7a6c69;
    --band: #7e6c68;
    --band-text: #ffffff;
    --frame: #ffffff;
  }
  * { box-sizing: border-box; margin: 0; padding: 0; }
  html, body { width: 1200px; height: 1000px; overflow: hidden; }
  body { background: var(--stage); position: relative; font-family: "Raleway", sans-serif; color: var(--ink); }

  .brochure { position: absolute; left: 55px; top: 80px; width: 1090px; height: 842px; background: var(--paper); overflow: hidden; }

  .panel { position: absolute; top: 0; height: 842px; }
  .panel--intro { left: 0; width: 390px; }
  .panel--contact { left: 390px; width: 336px; }
  .panel--cover { left: 726px; width: 364px; background: var(--paper); }

  .intro-backdrop { position: absolute; inset: 0; background: linear-gradient(160deg, #e9e6e3 0%, #f4f2f0 35%, #ece8e5 60%, #f6f5f4 100%); }
  .contact-backdrop { position: absolute; inset: 0; background: linear-gradient(180deg, #efecea 0%, #f4f2f1 60%, #ebe8e6 100%); }

  .intro-copy { position: absolute; left: 30px; top: 52px; width: 330px; }
  .headline { font-family: "Cinzel", serif; font-size: 22px; line-height: 33px; letter-spacing: 0.5px; color: var(--ink); margin-bottom: 32px; }
  .body-text { font-size: 15px; line-height: 19.5px; color: var(--ink-soft); }
  .body-text strong { font-weight: 800; color: var(--ink); }
  .room-title { font-family: "Cinzel", serif; font-size: 23px; line-height: 26px; color: var(--ink); margin-top: 10px; }
  .room-capacity { font-weight: 800; font-size: 15px; line-height: 19.5px; color: var(--ink); }
  .gap { margin-top: 19px; }

  .photo { position: absolute; border: 4px solid var(--frame); }
  .photo--bride { left: 3px; top: -4px; width: 304px; height: 316px; background: linear-gradient(135deg, #3b3531 0%, #8a7d72 45%, #d7d0c8 70%, #4a433e 100%); }
  .photo--bouquet { left: 3px; top: 312px; width: 304px; height: 230px; background: linear-gradient(120deg, #c9a9a1 0%, #efe7e3 40%, #f7f4f1 60%, #d6b7ae 100%); }

  .contact-copy { position: absolute; left: 1px; top: 568px; width: 330px; }
  .contact-lead { font-size: 15px; line-height: 19.5px; color: var(--ink-soft); margin-bottom: 20px; }
  .contact-web, .contact-name, .contact-venue { font-family: "Cinzel", serif; font-size: 16px; line-height: 20px; color: var(--ink); letter-spacing: 0.3px; }
  .contact-web { margin-bottom: 18px; }
  .contact-lines { font-size: 15px; line-height: 20px; color: var(--ink-soft); margin-bottom: 18px; }

  .cover-name { position: absolute; left: 0; top: 36px; width: 364px; text-align: center; font-family: "Cinzel", serif; font-size: 25px; line-height: 30px; color: var(--ink); }
  .cover-name .dot { display: inline-block; width: 12px; height: 12px; border-radius: 50%; background: var(--ink); margin-right: 8px; vertical-align: middle; }
  .cover-services { position: absolute; left: 0; top: 154px; width: 364px; text-align: center; font-family: "Cinzel", serif; font-size: 14px; line-height: 20px; letter-spacing: 0.4px; color: var(--ink); }
  .cover-services .sep { opacity: 0.5; margin: 0 4px; }
  .cover-rule { position: absolute; left: 42px; width: 280px; height: 1px; background: var(--ink); opacity: 0.5; }

  .cover-collage { position: absolute; left: 0; top: 225px; width: 364px; height: 516px; background: linear-gradient(150deg, #6f7a3e 0%, #b89a6e 35%, #e8ddd0 60%, #8a8c4c 100%); }
  .collage-frame { position: absolute; border: 4px solid var(--frame); }
  .collage-frame--couple { left: 24px; top: 52px; width: 158px; height: 406px; background: linear-gradient(160deg, #c9b59a 0%, #f1ece6 55%, #a4906f 100%); }
  .collage-frame--toast { left: 181px; top: 0; width: 157px; height: 202px; background: linear-gradient(135deg, #b89070 0%, #e8d6c4 50%, #8f6f55 100%); }
  .collage-frame--flowers { left: 181px; top: 311px; width: 157px; height: 205px; background: linear-gradient(135deg, #e6b8b0 0%, #f5ecea 45%, #5f7a44 100%); }

  .cover-band { position: absolute; left: 0; top: 741px; width: 364px; height: 101px; background: var(--band); color: var(--band-text); text-align: center; font-family: "Cinzel", serif; font-size: 17px; line-height: 26px; letter-spacing: 0.5px; padding-top: 11px; }
</style>
</head>
<body>
<main class="brochure">

  <section class="panel panel--intro">
    <div class="intro-backdrop" role="img" aria-label="Soft blurred photo of a wedding reception in pale whites"></div>
    <div class="intro-copy">
      <h1 class="headline">Host your event at<br>the Dallas area's<br>premiere event venue.</h1>
      <p class="body-text">The Event Hall at Willowbrook offers<br>a <strong>12,000 square foot</strong> facility which<br>boasts a Grand Ballroom and two<br>Banquet rooms.</p>
      <h2 class="room-title">The Grand Ballroom</h2>
      <p class="room-capacity">will accommodate 809 guests</p>
      <p class="body-text">for a wedding ceremony and<br>reception, quinceanera, retirement party<br>or any occasion that demands a<br>large-scale, elegant setting.</p>
      <p class="body-text gap"><strong>The bridal suite</strong> at the top of the<br>winding staircase allows the Bride and<br>her bridesmaids to prepare for the<br>big day out of sight of arriving guests,<br>allowing a dramatic grand entrance.</p>
      <h2 class="room-title">Banquet Room 1</h2>
      <p class="room-capacity">will accommodate 103 guests<br>for a mid-size, private event</p>
      <p class="body-text">such as a birthday or retirement party<br>or company holiday party.</p>
      <h2 class="room-title">Banquet Room 2</h2>
      <p class="room-capacity">will accommodate 35 guests<br>for a small intimate event</p>
      <p class="body-text">such as a bridal shower, bridesmaid's<br>luncheon or corporate training.</p>
      <p class="body-text gap">The rooms can be used separately<br>or together.</p>
    </div>
  </section>

  <section class="panel panel--contact">
    <div class="contact-backdrop" role="img" aria-label="Soft blurred wedding photo background"></div>
    <div class="photo photo--bride" role="img" aria-label="Photo of a bride wearing a veil"></div>
    <div class="photo photo--bouquet" role="img" aria-label="Photo of a bride and bridesmaids holding white bouquets"></div>
    <div class="contact-copy">
      <p class="contact-lead">Contact us for more information<br>or visit us at:</p>
      <p class="contact-web">www.eventhallwillowbrook.com</p>
      <p class="contact-name">Laura Benson</p>
      <p class="contact-lines">laura@eventhallwillowbrook.com<br>214-555-0142<br>972-555-0187</p>
      <p class="contact-venue">Event Hall at Willowbrook<br>4820 Meadow Lane Road<br>Kemp, TX 75143</p>
    </div>
  </section>

  <section class="panel panel--cover">
    <p class="cover-name"><span class="dot"></span>The Event Hall<br>at Willowbrook</p>
    <div class="cover-rule" style="top:146px"></div>
    <p class="cover-services">Wedding <span class="sep">|</span> Conference <span class="sep">|</span> Seminar <span class="sep">|</span> Party<br>Reunion <span class="sep">|</span> Graduation</p>
    <div class="cover-rule" style="top:200px"></div>
    <div class="cover-collage" role="img" aria-label="Outdoor wedding photo with falling petals">
      <div class="collage-frame collage-frame--couple" role="img" aria-label="Photo of a smiling bride and groom"></div>
      <div class="collage-frame collage-frame--toast" role="img" aria-label="Photo of guests raising champagne glasses"></div>
      <div class="collage-frame collage-frame--flowers" role="img" aria-label="Photo of a pink and white rose arrangement"></div>
    </div>
    <p class="cover-band">Host your event at<br>the Dallas area's premiere<br>event venue.</p>
  </section>

</main>
</body>
</html>
```